Web site for a company that sells Pinball machines

We need a website that is an online shopping experience for a Store that sells pinball machines and accessories. The name of the store is called "Bumper Vault Arcade." The store it self has a showroom, but we would also like to have an Internet e-commerce presence. We pinball machines made by Halvern gameworks. You can visit their website and see their current list of machines as well as their website for the machines that we are going to carry in our store. Their website is Halverngameworks.example. I am able to use their machine photos as well as their machine brochure PDF files. I am also able to use their logo on my website two list it as a Halvern Authorized Dealer.
This website design needs to be funky, fun, very technologically oriented and modern. The people buying machines our spending anywhere between $5000 and $15,000 on one machine. These Are high-end buyers who are also usually fairly tech savvy or at least enjoy technology and graphics.
Attachments: I have attached photographs of some of my own machines which may be used in the website. I've also attached some downloaded files from Halvern gameworks.example as well as some of their PDF files for brochures. I will carry all of their current models they have listed under games. Not the archived games. I have included one of their machines called Copperfield Limited edition in my photograph attachments. The rest of the photos are just random pictures that I have taken myself and maybe used to build the site. Lastly I have attached my logo which I am not super crazy about so I will also be posting a contest to redesign this logo. Tons more of my own pinball photos are available.
I would like for people to be able to purchase machines and accessories from the website, but also inform them to our actual showroom.
Updates
Target Market(s)
Target market is 16 to 75. Techy individuals to enjoy gaming technology video animation and Vegas style twinkle
Industry/Entity Type
It Company
Coding
Coded - Design and coding required
Number of Pages Required
3 page
Look and feel

```html
<!DOCTYPE html>
<html lang="en">
<head>
<meta charset="utf-8">
<title>Bumper Vault Arcade</title>
<link rel="stylesheet" href="https://fonts.googleapis.com/css2?family=Oswald:wght@500;700&family=Open+Sans:wght@400;600;700&display=swap">
<style>
  :root {
    --page: #1d2129;
    --topbar: #15181d;
    --navbar: #22262d;
    --searchbar: #1a1d23;
    --footer: #16191e;
    --footer-base: #101216;
    --heading: #8ea6cc;
    --text: #d6d9de;
    --muted: #9aa0aa;
    --red: #e0262b;
    --price: #d8262c;
    --line: #323741;
    --button: #3a4049;
    --white: #ffffff;
  }
  * { box-sizing: border-box; margin: 0; padding: 0; }
  html, body { width: 1200px; height: 3082px; overflow: hidden; }
  body {
    background: var(--page);
    color: var(--text);
    font-family: "Open Sans", Arial, sans-serif;
    position: relative;
  }
  .abs { position: absolute; }

  /* Top utility bar */
  .utility-bar { left: 0; top: 0; width: 1200px; height: 47px; background: var(--topbar); }
  .utility-icons { right: 55px; top: 12px; display: flex; gap: 15px; align-items: center; }
  .utility-icons .sep { width: 1px; height: 16px; background: #4a4f58; }

  /* Main navigation */
  .site-header { left: 0; top: 47px; width: 1200px; height: 105px; background: var(--navbar); }
  .brand { left: 55px; top: 30px; display: flex; align-items: center; gap: 10px; }
  .brand-dot { width: 20px; height: 20px; border-radius: 50%; background: var(--red); }
  .brand-name { font-family: "Open Sans", sans-serif; font-weight: 700; font-size: 19px; color: var(--white); line-height: 1.15; width: 120px; }
  .main-nav { right: 55px; top: 43px; display: flex; gap: 41px; }
  .main-nav a { color: var(--white); text-decoration: none; font-size: 15px; font-weight: 400; letter-spacing: 0.3px; }

  /* Search band */
  .search-band { left: 0; top: 152px; width: 1200px; height: 84px; background: var(--searchbar); }
  .search-box { left: 555px; top: 21px; width: 497px; height: 45px; background: #2c3139; border-radius: 6px; }
  .search-box span { position: absolute; left: 38px; top: 13px; font-size: 14px; color: #8a909a; letter-spacing: 0.4px; }
  .search-go { position: absolute; right: 0; top: 0; width: 64px; height: 45px; background: #3c424b; border-radius: 0 6px 6px 0; }
  .cart { left: 1091px; top: 20px; width: 50px; height: 47px; background: #262a31; border-radius: 5px; }
  .cart-count { position: absolute; right: 2px; top: 2px; width: 16px; height: 16px; border-radius: 50%; background: #5b6270; font-size: 9px; color: var(--white); text-align: center; line-height: 16px; }

  /* Hero */
  .hero { left: 0; top: 236px; width: 1200px; height: 411px;
    background: radial-gradient(ellipse at 55% 40%, #5b3e7a 0%, #3f2c5a 45%, #2a2338 100%); }
  .hero-title { left: 55px; font-family: "Open Sans", sans-serif; font-size: 46px; color: var(--white); padding: 0 12px; height: 58px; line-height: 56px; }
  .hero-title.first { top: 152px; background: var(--red); }
  .hero-title.second { top: 228px; background: #1b1d22; }
  .hero-machines { left: 514px; top: 31px; width: 629px; height: 319px;
    background: linear-gradient(90deg, #5d4a9a 0%, #7a5fb6 30%, #3e3570 50%, #7a5fb6 70%, #5d4a9a 100%); border-radius: 4px; opacity: 0.9; }
  .hero-dots { left: 570px; top: 388px; display: flex; gap: 14px; }
  .hero-dots i { width: 9px; height: 9px; border-radius: 50%; background: #7b7390; display: block; }
  .hero-dots i.active { background: var(--white); }

  /* Section headings */
  .section-title { font-family: "Oswald", sans-serif; font-weight: 700; color: var(--heading); font-size: 37px; line-height: 1; }
  .centered { left: 0; width: 1200px; text-align: center; }
  .divider { left: 55px; width: 1088px; height: 1px; background: var(--line); }

  .about-copy { left: 60px; top: 736px; width: 1080px; text-align: center; font-size: 21px; line-height: 35px; color: var(--text); }

  /* Games */
  .game-card { top: 1021px; width: 254px; }
  .game-image { width: 254px; height: 241px; }
  .game-name { margin-top: 12px; font-size: 16px; line-height: 25px; color: var(--text); }
  .game-platform { margin-top: 8px; font-size: 14px; color: var(--muted); }
  .game-price { margin-top: 10px; font-size: 24px; font-weight: 700; color: var(--price); }
  .view-more { left: 476px; top: 1426px; width: 248px; height: 62px; background: var(--button); border-radius: 8px;
    font-family: "Oswald", sans-serif; font-weight: 700; font-size: 23px; color: #c4cfdf; text-align: center; line-height: 62px; }

  /* Showroom & video */
  .showroom-copy { left: 55px; top: 1628px; width: 540px; font-size: 20px; line-height: 35px; color: var(--text); }
  .showroom-photo { left: 55px; top: 1773px; width: 502px; height: 294px;
    background: linear-gradient(180deg, #5a1e1e 0%, #8a2a22 40%, #3a1a18 75%, #1a1414 100%); }
  .video { left: 631px; top: 1642px; width: 514px; height: 425px;
    background: linear-gradient(160deg, #3b3555 0%, #5a4a5e 40%, #6c5a4c 70%, #3a3030 100%); }
  .video-play { position: absolute; left: 212px; top: 100px; }
  .video-controls { position: absolute; left: 0; bottom: 0; width: 514px; height: 43px; background: #0d0f12; }
  .video-controls .time { position: absolute; top: 21px; font-size: 12px; color: #cfd3da; }

  /* Posts */
  .posts-rule { left: 55px; top: 2172px; width: 1024px; height: 2px; background: var(--line); }
  .posts-rule-accent { left: 55px; top: 2171px; width: 167px; height: 5px; background: var(--red); }
  .posts-arrows { left: 1103px; top: 2165px; display: flex; gap: 4px; }
  .posts-arrows span { width: 18px; height: 18px; background: #3a3f48; display: block; }
  .post-card { top: 2215px; width: 346px; }
  .post-image { width: 346px; height: 339px; }
  .post-title { margin-top: 20px; padding-left: 3px; font-size: 22px; font-weight: 700; line-height: 31px; color: var(--white); }
  .post-meta { margin-top: 19px; display: flex; align-items: center; gap: 10px; font-size: 20px; color: var(--text); }

  /* Footer */
  .footer { left: 0; top: 2725px; width: 1200px; height: 296px; background: var(--footer); }
  .footer h4 { position: absolute; top: 30px; font-family: "Oswald", sans-serif; font-weight: 700; font-size: 17px; color: var(--white); letter-spacing: 0.3px; }
  .footer-brand { left: 55px; top: 86px; display: flex; align-items: center; gap: 10px; }
  .footer-about { left: 55px; top: 172px; width: 340px; font-size: 14px; line-height: 29px; color: #c8ccd2; }
  .footer-links { list-style: none; font-size: 13px; color: #d4d7dc; }
  .footer-links.col-a { left: 491px; top: 70px; line-height: 33px; }
  .footer-links.col-b { left: 664px; top: 66px; line-height: 46.5px; }
  .newsletter-copy { left: 917px; top: 70px; width: 260px; font-size: 14px; line-height: 25px; color: #d4d7dc; }
  .newsletter-input { left: 919px; top: 148px; width: 224px; height: 34px; background: var(--white); border-radius: 3px; font-size: 12px; color: #333; padding: 8px 10px; }
  .subscribe { left: 919px; top: 214px; width: 224px; height: 34px; background: var(--red); border-radius: 3px; font-size: 12px; color: var(--white); text-align: center; line-height: 34px; }

  .footer-base { left: 0; top: 3021px; width: 1200px; height: 61px; background: var(--footer-base); }
  .copyright { position: absolute; left: 57px; top: 21px; font-size: 14px; color: #c8ccd2; }
  .social { position: absolute; right: 63px; top: 22px; display: flex; gap: 16px; }
  .social i { width: 14px; height: 14px; border-radius: 50%; background: #6a707b; display: block; }
  .social i.first { background: var(--red); }
</style>
</head>
<body>

<div class="abs utility-bar">
  <div class="abs utility-icons">
    <svg width="16" height="16" viewBox="0 0 16 16" aria-label="Account"><circle cx="8" cy="5" r="3.5" fill="#8a909a"/><path d="M1 16c0-4 3-6 7-6s7 2 7 6z" fill="#8a909a"/></svg>
    <span class="sep"></span>
    <svg width="16" height="16" viewBox="0 0 16 16" aria-label="Search"><circle cx="6.5" cy="6.5" r="4.5" fill="none" stroke="#8a909a" stroke-width="2"/><path d="M10 10l5 5" stroke="#8a909a" stroke-width="2.4"/></svg>
    <span class="sep"></span>
    <svg width="18" height="16" viewBox="0 0 18 16" aria-label="Gallery"><rect x="1" y="1" width="16" height="14" rx="2" fill="none" stroke="#8a909a" stroke-width="2"/><path d="M3 13l4-5 3 3 2-2 3 4z" fill="#8a909a"/></svg>
    <span class="sep"></span>
    <svg width="18" height="14" viewBox="0 0 18 14" aria-label="Mail"><rect x="0" y="0" width="18" height="14" rx="1" fill="#8a909a"/><path d="M1 1l8 7 8-7" fill="none" stroke="#15181d" stroke-width="1.6"/></svg>
  </div>
</div>

<header class="abs site-header">
  <div class="abs brand">
    <span class="brand-dot"></span>
    <span class="brand-name">Bumper Vault Arcade</span>
  </div>
  <nav class="abs main-nav">
    <a href="#">HOME</a><a href="#">ABOUT</a><a href="#">GAMES</a><a href="#">COMMUNITY</a><a href="#">SUPPORT</a><a href="#">CONTACT US</a><a href="#">BUY</a>
  </nav>
</header>

<div class="abs search-band">
  <div class="abs search-box">
    <span>ALL CATEGORIES</span>
    <div class="search-go"><svg width="64" height="45" viewBox="0 0 64 45"><path d="M28 16l7 6.5-7 6.5" fill="none" stroke="#d0d4da" stroke-width="2"/></svg></div>
  </div>
  <div class="abs cart">
    <svg width="50" height="47" viewBox="0 0 50 47"><path d="M15 17h4l3 11h11l3-8H21" fill="none" stroke="#7d838d" stroke-width="2"/><circle cx="23" cy="32" r="1.8" fill="#7d838d"/><circle cx="32" cy="32" r="1.8" fill="#7d838d"/></svg>
    <span class="cart-count">0</span>
  </div>
</div>

<section class="abs hero">
  <div class="abs hero-machines" role="img" aria-label="Three purple pinball machines standing side by side"></div>
  <div class="abs hero-title first">Lorem ipsum dolor</div>
  <div class="abs hero-title second">sit amet consec</div>
  <div class="abs hero-dots"><i></i><i></i><i class="active"></i></div>
</section>

<h2 class="abs section-title centered" style="top:684px">About Bumper Vault Arcade</h2>
<p class="abs about-copy">Lorem ipsum dolor sit amet, consectetur adipiscing elit. Nullam tortor nisl, suscipit id nunc sit amet,<br>facilisis tincidunt augue. Suspendisse rhoncus lacus et est ultrices, at volutpat tortor faucibus.<br>Nunc pharetra orci id eros dictum, at tincidunt libero pulvinar. Morbi suscipit fermentum<br>Nam maximus nibh vehicula porta bibendum.</p>
<div class="abs divider" style="top:910px"></div>

<h2 class="abs section-title centered" style="top:945px">GamEs</h2>

<article class="abs game-card" style="left:55px">
  <div class="game-image" role="img" aria-label="Close-up of a pinball playfield with flippers and bumpers" style="background:linear-gradient(150deg,#6a2a40,#8a4a7a 45%,#2e2a4a)"></div>
  <p class="game-name">Lorem ipsum dolor sit amet sectetur adipiscing elit.</p>
  <p class="game-platform">ARCADE 360</p>
  <p class="game-price">$59.00</p>
</article>
<article class="abs game-card" style="left:333px">
  <div class="game-image" role="img" aria-label="Pinball playfield with a red bumper and inserts" style="background:linear-gradient(150deg,#7a5a1a,#b08a2a 45%,#3a2a1a)"></div>
  <p class="game-name">Lorem ipsum dolor sit amet sectetur adipiscing elit.</p>
  <p class="game-platform">ARCADE 360</p>
  <p class="game-price">$59.00</p>
</article>
<article class="abs game-card" style="left:610px">
  <div class="game-image" role="img" aria-label="Colourful pinball playfield artwork" style="background:linear-gradient(150deg,#4a5a3a,#7a6a4a 45%,#2a3a4a)"></div>
  <p class="game-name">Lorem ipsum dolor sit amet sectetur adipiscing elit.</p>
  <p class="game-platform">ARCADE 360</p>
  <p class="game-price">$59.00</p>
</article>
<article class="abs game-card" style="left:890px">
  <div class="game-image" role="img" aria-label="Purple pinball playfield with a red bumper" style="background:linear-gradient(150deg,#4a2a6a,#8a3a6a 45%,#2a2040)"></div>
  <p class="game-name">Lorem ipsum dolor sit amet sectetur adipiscing elit.</p>
  <p class="game-platform">ARCADE 360</p>
  <p class="game-price">$59.00</p>
</article>

<div class="abs view-more">VIEW MORE</div>
<div class="abs divider" style="top:1529px"></div>

<h2 class="abs section-title" style="left:55px;top:1568px">Our Showroom</h2>
<h2 class="abs section-title" style="left:629px;top:1568px">LATEST VIDEO</h2>
<p class="abs showroom-copy">consectetur adipiscing elit. Nullam tortor nisl suscipit<br>id nunc sit amet, facilisis tincidunt augue<br>Suspendisse rhoncus lacus.</p>
<div class="abs showroom-photo" role="img" aria-label="Row of pinball machines in the showroom"></div>

<div class="abs video" role="img" aria-label="Video still of a pinball playfield">
  <svg class="video-play" width="90" height="90" viewBox="0 0 90 90"><circle cx="45" cy="45" r="43" fill="#1a1c22" fill-opacity="0.75"/><path d="M36 28l28 17-28 17z" fill="var(--red)"/></svg>
  <div class="video-controls">
    <svg width="514" height="43" viewBox="0 0 514 43">
      <rect x="14" y="10" width="4" height="14" fill="#fff"/><rect x="21" y="10" width="4" height="14" fill="#fff"/>
      <rect x="34" y="10" width="2" height="14" fill="#fff"/><path d="M44 10v14l-8-7z" fill="#fff"/>
      <rect x="54" y="10" width="2" height="14" fill="#fff"/><path d="M64 10v14l-8-7z" fill="#fff"/>
      <rect x="80" y="15" width="370" height="4" fill="#555a63"/><rect x="80" y="15" width="175" height="4" fill="var(--red)"/>
      <path d="M466 14h4l5-4v14l-5-4h-4z" fill="#fff"/>
      <path d="M490 10h5M490 10v5M504 10h-5M504 10v5M490 24h5M490 24v-5M504 24h-5M504 24v-5" stroke="#fff" stroke-width="2.4" fill="none"/>
    </svg>
    <span class="time" style="left:118px">00:34</span>
    <span class="time" style="left:414px">00:34</span>
  </div>
</div>

<h2 class="abs section-title" style="left:55px;top:2103px;color:#a9bcd9">LATEST POSTS</h2>
<div class="abs posts-rule"></div>
<div class="abs posts-rule-accent"></div>
<div class="abs posts-arrows">
  <span><svg width="18" height="18"><path d="M11 5l-4 4 4 4" stroke="#8a909a" fill="none" stroke-width="1.6"/></svg></span>
  <span><svg width="18" height="18"><path d="M7 5l4 4-4 4" stroke="#8a909a" fill="none" stroke-width="1.6"/></svg></span>
</div>

<article class="abs post-card" style="left:55px">
  <div class="post-image" role="img" aria-label="Pinball cabinet toy figure and playfield detail" style="background:linear-gradient(160deg,#4a3a6a,#6a4a8a 40%,#3a4a5a)"></div>
  <h3 class="post-title">Lorem ipsum dolor sit amet sectetur adipiscing elit.</h3>
  <div class="post-meta">
    <svg width="22" height="22" viewBox="0 0 22 22"><rect x="1" y="3" width="20" height="18" rx="2" fill="none" stroke="#b8bdc6" stroke-width="2"/><path d="M1 8h20M6 1v4M16 1v4" stroke="#b8bdc6" stroke-width="2"/><path d="M5 12h3M10 12h3M15 12h3M5 16h3M10 16h3" stroke="#b8bdc6" stroke-width="2"/></svg>
    <span>Mar&nbsp; 17,0217</span>
    <svg width="24" height="20" viewBox="0 0 24 20" style="margin-left:10px"><ellipse cx="12" cy="9" rx="11" ry="8" fill="#b8bdc6"/><path d="M4 14l-2 6 7-4z" fill="#b8bdc6"/></svg>
    <span>7</span>
  </div>
</article>
<article class="abs post-card" style="left:427px">
  <div class="post-image" role="img" aria-label="Coin door on a red pinball cabinet" style="background:linear-gradient(160deg,#5a1a1a,#9a2a22 45%,#3a1212)"></div>
  <h3 class="post-title">Lorem ipsum dolor sit amet sectetur adipiscing elit.</h3>
  <div class="post-meta">
    <svg width="22" height="22" viewBox="0 0 22 22"><rect x="1" y="3" width="20" height="18" rx="2" fill="none" stroke="#b8bdc6" stroke-width="2"/><path d="M1 8h20M6 1v4M16 1v4" stroke="#b8bdc6" stroke-width="2"/><path d="M5 12h3M10 12h3M15 12h3M5 16h3M10 16h3" stroke="#b8bdc6" stroke-width="2"/></svg>
    <span>Mar&nbsp; 17,0217</span>
    <svg width="24" height="20" viewBox="0 0 24 20" style="margin-left:10px"><ellipse cx="12" cy="9" rx="11" ry="8" fill="#b8bdc6"/><path d="M4 14l-2 6 7-4z" fill="#b8bdc6"/></svg>
    <span>7</span>
  </div>
</article>
<article class="abs post-card" style="left:799px">
  <div class="post-image" role="img" aria-label="Blurred arcade floor with lit machines" style="background:linear-gradient(160deg,#4a4a6a,#8a5a5a 45%,#3a4a4a)"></div>
  <h3 class="post-title">Lorem ipsum dolor sit amet sectetur adipiscing elit.</h3>
  <div class="post-meta">
    <svg width="22" height="22" viewBox="0 0 22 22"><rect x="1" y="3" width="20" height="18" rx="2" fill="none" stroke="#b8bdc6" stroke-width="2"/><path d="M1 8h20M6 1v4M16 1v4" stroke="#b8bdc6" stroke-width="2"/><path d="M5 12h3M10 12h3M15 12h3M5 16h3M10 16h3" stroke="#b8bdc6" stroke-width="2"/></svg>
    <span>Mar&nbsp; 17,0217</span>
    <svg width="24" height="20" viewBox="0 0 24 20" style="margin-left:10px"><ellipse cx="12" cy="9" rx="11" ry="8" fill="#b8bdc6"/><path d="M4 14l-2 6 7-4z" fill="#b8bdc6"/></svg>
    <span>7</span>
  </div>
</article>

<footer class="abs footer">
  <h4 style="left:55px">ABOUT</h4>
  <h4 style="left:491px">QUICK LINKS</h4>
  <h4 style="left:917px">NEWSLETTER</h4>
  <div class="abs footer-brand">
    <span class="brand-dot"></span>
    <span class="brand-name">Bumper Vault Arcade</span>
  </div>
  <p class="abs footer-about">consectetur adipiscing elit. Nullam tortor nisl<br>suscipit id nunc sit amet, facilisis tincidunt<br>augue Suspendisse rhoncus lacus.</p>
  <ul class="abs footer-links col-a">
    <li>HOME</li><li>ABOUT</li><li>GAMES</li><li>COMMUNITY</li><li>SUPPORT</li><li>BUY</li>
  </ul>
  <ul class="abs footer-links col-b">
    <li>OUR PARTNERS</li><li>PRIVACY POLICY/</li><li>TERMS OF SERVICE</li><li>CONTACT US</li>
  </ul>
  <p class="abs newsletter-copy">Enter your e-mail and subscribe<br>to our newsletter</p>
  <div class="abs newsletter-input">E - mail</div>
  <div class="abs subscribe">SUBSCRIBE</div>
</footer>

<div class="abs footer-base">
  <p class="copyright">Copyrights © 2017 &amp; All Rights Reserved by</p>
  <div class="social" aria-label="Social links"><i class="first"></i><i></i><i></i><i></i><i></i><i></i></div>
</div>

</body>
</html>
```